Lower-middle market private equity firm needs its PowerPoint template update/refresh

Wexford Lindqvist Capital Partners is a lower-middle market private equity firm focused on acquiring family- and founder-owned businesses in the industrial market. Website is here for more info: https://www.wlcpx-example.com/. We would like to upgrade/update our powerpoint template/slide master we use for marketing materials - uploading a powerpoint version with some of the slide templates we use. We would like to keep it classic and clean with a white background and color on top and enough room for text on the pages. We would prefer to stay within the color palette of the hash tag logo on the cover page (cover page needs an update as well). We are open to suggestions on the font we utilize as well.

```html
<!DOCTYPE html>
<html lang="en">
<head>
<meta charset="utf-8">
<title>Wexford Lindqvist Capital Partners – Presentation Template</title>
<link href="https://fonts.googleapis.com/css2?family=Archivo:wght@500;700;800;900&family=Inter:ital,wght@0,400;0,500;0,600;0,700;1,400&display=swap" rel="stylesheet">
<style>
:root{
  --navy:#1b5e80;
  --navy-dark:#134a66;
  --gold:#b4a432;
  --green:#2f7d57;
  --green-dark:#25653f;
  --sky:#4a90d0;
  --beige:#f4f1ee;
  --beige-band:#e9e5e0;
  --ink:#222;
  --muted:#8a8a8a;
  --page:#ebebeb;
}
*{margin:0;padding:0;box-sizing:border-box}
html,body{width:1200px;height:2489px;overflow:hidden;background:var(--page)}
body{font-family:'Inter',sans-serif;color:var(--ink)}
.deck{position:absolute;left:77px;top:187px;display:grid;grid-template-columns:repeat(3,337px);column-gap:18px;grid-auto-rows:252px;row-gap:57px}
.slide{position:relative;background:#fff;overflow:hidden}
.slide::before{content:"";position:absolute;left:14px;right:14px;top:0;height:2px;background:linear-gradient(90deg,var(--green) 0 30%,var(--gold) 30% 62%,var(--sky) 62% 100%);z-index:2}
.abs{position:absolute}
.wordmark{position:absolute;font-family:'Archivo',sans-serif;font-weight:800;color:var(--navy);font-size:7px;line-height:1.05;letter-spacing:.3px;display:flex;align-items:center;gap:4px}
.wordmark .dot{width:9px;height:9px;background:var(--gold);flex:none}
.h-title{position:absolute;left:16px;top:20px;font-family:'Archivo',sans-serif;font-weight:800;font-size:11px;color:var(--navy)}
.h-sub{position:absolute;left:16px;top:35px;font-size:7px;font-weight:600;color:#333}
.h-rule{position:absolute;left:16px;top:46px;width:305px;height:.6px;background:#bdbdbd}
.h-rule.short{width:150px}
.gold-head{position:absolute;font-weight:700;font-size:6.5px;color:var(--gold)}
.list{position:absolute;list-style:none;font-size:5.3px;line-height:1.3;color:#222}
.list li{position:relative;padding-left:8px;margin-bottom:3px}
.list li::before{content:"›";position:absolute;left:0;top:-1px;color:var(--gold);font-size:7px}
.list li.sub{padding-left:24px;margin-top:-2px}
.list li.sub::before{left:16px}
.note{position:absolute;left:16px;bottom:14px;font-size:3.2px;color:#aaa}
.foot{position:absolute;left:14px;right:14px;bottom:0;height:9px;background:#f2f2f2;display:flex;align-items:center;justify-content:space-between;padding:0 4px;font-size:3.2px;color:#555;font-weight:600}
.ph{position:absolute}
.ph-gray{background:linear-gradient(135deg,#8e9aa6,#5d6b78)}
.ph-teal{background:linear-gradient(135deg,#2c6b8a,#9ec4d6)}
.ph-warm{background:linear-gradient(135deg,#c9a873,#5a5040)}
.ph-green{background:linear-gradient(135deg,#3b5d4e,#8fb3a7)}
.ph-dark{background:linear-gradient(135deg,#1f2b38,#6b7f8e)}
.cover-title{position:absolute;font-family:'Archivo',sans-serif;font-weight:800;color:var(--navy);line-height:1.1}
.cover-italic{position:absolute;font-style:italic;font-size:6.5px;color:#333;line-height:1.3}
.values{position:absolute;display:flex;font-size:3.6px;color:#333}
.values span{padding:0 12px;border-right:.8px solid #333;line-height:7px}
.values span:first-child{padding-left:0}
.values span:last-child{border:none}
.divider-title{position:absolute;font-family:'Archivo',sans-serif;font-weight:800;font-size:12.5px;color:#fff;line-height:1.15}
.card-shadow{box-shadow:0 0 3px rgba(0,0,0,.15);background:#fff}
.tiny{font-size:3.6px;line-height:1.35;color:#333}
</style>
</head>
<body>
<main class="deck">

<!-- 1 Cover, light panel -->
<section class="slide">
  <div class="abs" style="left:14px;top:14px;width:309px;height:222px;background:var(--beige)"></div>
  <div class="wordmark" style="left:26px;top:30px"><span class="dot"></span><span>WEXFORD<br>LINDQVIST<br><small style="font-size:4px;color:var(--gold)">CAPITAL PARTNERS</small></span></div>
  <div class="abs" style="left:14px;top:98px;width:230px;height:56px;background:var(--beige-band)"></div>
  <div class="cover-title" style="left:26px;top:112px;font-size:11px">Realizing the promise in small<br>companies for decades</div>
  <div class="cover-italic" style="left:28px;top:167px">Realizing the promise in<br>small companies for decades</div>
  <div class="values" style="left:28px;top:198px"><span>Perseverance</span><span>Ingenuity</span><span>Transparency</span><span>Results</span></div>
</section>

<!-- 2 Cover, photo -->
<section class="slide" style="background:var(--beige)">
  <div class="wordmark" style="left:18px;top:18px"><span class="dot"></span><span>WEXFORD<br>LINDQVIST<br><small style="font-size:4px;color:var(--gold)">CAPITAL PARTNERS</small></span></div>
  <div class="ph ph-dark" role="img" aria-label="Photo of an engineer in a hard hat at an industrial site" style="left:165px;top:0;width:172px;height:252px;clip-path:polygon(42% 0,100% 0,100% 100%,0 100%)"></div>
  <div class="cover-title" style="left:18px;top:85px;font-size:12px">Realizing the promise<br>in small companies<br>for decades</div>
  <div class="abs" style="left:0;top:178px;width:200px;height:52px;background:var(--beige-band);clip-path:polygon(0 0,100% 0,86% 100%,0 100%)"></div>
  <div class="cover-italic" style="left:18px;top:186px">Realizing the promise in<br>small companies for decades</div>
  <div class="values" style="left:18px;top:214px"><span style="padding:0 6px 0 0">Perseverance</span><span style="padding:0 6px">Ingenuity</span><span style="padding:0 6px">Transparency</span><span style="padding:0 6px">Results</span></div>
</section>

<!-- 3 Cover, photo block -->
<section class="slide">
  <div class="abs" style="left:14px;top:14px;width:309px;height:222px;background:var(--beige)"></div>
  <div class="wordmark" style="left:26px;top:30px"><span class="dot"></span><span>WEXFORD<br>LINDQVIST<br><small style="font-size:4px;color:var(--gold)">CAPITAL PARTNERS</small></span></div>
  <div class="abs" style="left:14px;top:98px;width:240px;height:56px;background:var(--beige-band)"></div>
  <div class="ph ph-teal" role="img" aria-label="Photo of factory machinery with digital overlay" style="left:256px;top:72px;width:67px;height:108px"></div>
  <div class="cover-title" style="left:26px;top:112px;font-size:11px">Realizing the promise in small<br>companies for decades</div>
  <div class="cover-italic" style="left:28px;top:167px">Realizing the promise in<br>small companies for decades</div>
  <div class="values" style="left:28px;top:198px"><span>Perseverance</span><span>Ingenuity</span><span>Transparency</span><span>Results</span></div>
  <div class="abs" style="right:16px;bottom:4px;font-size:3.4px;color:#555">3</div>
</section>

<!-- 4 Table of content -->
<section class="slide">
  <div class="cover-title" style="left:16px;top:102px;font-size:13.5px">Table<br>of Content</div>
  <div class="abs" style="left:152px;top:36px;width:146px">
    <div style="display:flex;flex-direction:column;gap:0">
      <div style="display:flex;align-items:center;gap:6px;height:33px;border-bottom:.6px solid #999;font-size:5.5px"><b style="color:var(--gold);font-size:10px;font-family:Archivo,sans-serif">1</b>Lorem ipsum dolor sit amet</div>
      <div style="display:flex;align-items:center;gap:6px;height:33px;border-bottom:.6px solid #999;font-size:5.5px"><b style="color:var(--gold);font-size:10px;font-family:Archivo,sans-serif">2</b>Consectetur adipiscing elit</div>
      <div style="display:flex;align-items:center;gap:6px;height:33px;border-bottom:.6px solid #999;font-size:5.5px"><b style="color:var(--gold);font-size:10px;font-family:Archivo,sans-serif">3</b>Phasellus malesuada vulputate mauris</div>
      <div style="display:flex;align-items:center;gap:6px;height:33px;border-bottom:.6px solid #999;font-size:5.5px"><b style="color:var(--gold);font-size:10px;font-family:Archivo,sans-serif">4</b>Vitae pretium felis vestibulum vel</div>
      <div style="display:flex;align-items:center;gap:6px;height:33px;border-bottom:.6px solid #999;font-size:5.5px"><b style="color:var(--gold);font-size:10px;font-family:Archivo,sans-serif">5</b>Vestibulum non sagittis orci</div>
      <div style="display:flex;align-items:center;gap:6px;height:33px;font-size:5.5px"><b style="color:var(--gold);font-size:10px;font-family:Archivo,sans-serif">6</b>Fusce finibus elit et felis imperdiet</div>
    </div>
  </div>
  <div class="note">Footnote sample: Lorem ipsum dolor sit amet, te ullum corpora delicata duo.</div>
  <div class="foot"><span>WEXFORD LINDQVIST CAPITAL PARTNERS</span><span>CONFIDENTIAL</span><span>wlcpx-example.com &nbsp; 4</span></div>
</section>

<!-- 5 Divider navy -->
<section class="slide">
  <div class="abs" style="left:14px;top:14px;width:194px;height:222px;background:var(--navy)"></div>
  <div class="abs" style="left:14px;top:82px;width:194px;height:60px;background:var(--navy-dark)"></div>
  <div class="ph ph-teal" role="img" aria-label="Photo of a hand holding a glowing light bulb with technology icons" style="left:208px;top:14px;width:115px;height:222px"></div>
  <div class="divider-title" style="left:26px;top:98px">Divider Slide<br>Text Here</div>
  <div class="abs" style="left:26px;top:182px;font-size:5px;color:#fff">Lorem Ipsum is simply dummy text</div>
  <div class="foot"><span>WEXFORD LINDQVIST CAPITAL PARTNERS</span><span>CONFIDENTIAL</span><span>wlcpx-example.com &nbsp; 5</span></div>
</section>

<!-- 6 One column -->
<section class="slide">
  <div class="h-title">One Column Sample</div>
  <div class="h-sub">Sub Title Goes Here</div>
  <div class="h-rule"></div>
  <div class="gold-head" style="left:16px;top:60px">Heading Title Here</div>
  <ul class="list" style="left:16px;top:74px;width:300px">
    <li>Lorem ipsum dolor sit amet, te ullum corpora delicata duo. Rebum insolens pri eu.<br>No alia tota modus qui.</li>
    <li class="sub">Sint brute at usu. Duo iisque appareat adversarium at.</li>
    <li>Lorem ipsum dolor sit amet, te ullum corpora delicata duo. Rebum insolens pri eu.<br>No alia tota modus qui.</li>
    <li class="sub">Sint brute at usu. Duo iisque appareat adversarium at.</li>
    <li>Lorem ipsum dolor sit amet, te ullum corpora delicata duo. Rebum insolens pri eu.<br>No alia tota modus qui.</li>
    <li class="sub">Sint brute at usu. Duo iisque appareat adversarium at.</li>
    <li>Lorem ipsum dolor sit amet, te ullum corpora delicata duo. Rebum insolens pri eu.<br>No alia tota modus qui.</li>
  </ul>
  <div class="note">Footnote sample: Lorem ipsum dolor sit amet, te ullum corpora delicata duo.</div>
  <div class="foot"><span>WEXFORD LINDQVIST CAPITAL PARTNERS</span><span>CONFIDENTIAL</span><span>wlcpx-example.com &nbsp; 6</span></div>
</section>

<!-- 7 Three horizontal -->
<section class="slide">
  <div class="h-title">Three Horizontal Sample</div>
  <div class="h-sub">Sub Title Goes Here</div>
  <div class="h-rule"></div>
  <div class="gold-head" style="left:16px;top:60px">Heading Title Here</div>
  <div class="abs" style="left:16px;top:74px;width:305px;display:flex;flex-direction:column;gap:4px">
    <div class="card-shadow" style="display:flex;height:33px;align-items:center;font-size:4.6px"><div style="width:68px;height:33px;background:var(--navy);color:#fff;font-weight:700;font-size:5px;display:flex;align-items:center;justify-content:center;text-align:center">Text Title<br>Content 1</div><div style="padding-left:8px">Lorem ipsum dolor sit amet, te ullum corpora delicata duo. Rebum insolens pri eu.<br>No alia tota modus qui.</div></div>
    <div class="card-shadow" style="display:flex;height:33px;align-items:center;font-size:4.6px"><div style="width:68px;height:33px;background:var(--gold);color:#fff;font-weight:700;font-size:5px;display:flex;align-items:center;justify-content:center;text-align:center">Text Title<br>Content 2</div><div style="padding-left:8px">Lorem ipsum dolor sit amet, te ullum corpora delicata duo. Rebum insolens pri eu.<br>No alia tota modus qui.</div></div>
    <div class="card-shadow" style="display:flex;height:33px;align-items:center;font-size:4.6px"><div style="width:68px;height:33px;background:var(--navy);color:#fff;font-weight:700;font-size:5px;display:flex;align-items:center;justify-content:center;text-align:center">Text Title<br>Content 3</div><div style="padding-left:8px">Lorem ipsum dolor sit amet, te ullum corpora delicata duo. Rebum insolens pri eu.<br>No alia tota modus qui.</div></div>
    <div class="card-shadow" style="display:flex;height:33px;align-items:center;font-size:4.6px"><div style="width:68px;height:33px;background:var(--gold);color:#fff;font-weight:700;font-size:5px;display:flex;align-items:center;justify-content:center;text-align:center">Text Title<br>Content 4</div><div style="padding-left:8px">Lorem ipsum dolor sit amet, te ullum corpora delicata duo. Rebum insolens pri eu.<br>No alia tota modus qui.</div></div>
  </div>
  <div class="note">Footnote sample: Lorem ipsum dolor sit amet, te ullum corpora delicata duo.</div>
  <div class="foot"><span>WEXFORD LINDQVIST CAPITAL PARTNERS</span><span>CONFIDENTIAL</span><span>wlcpx-example.com &nbsp; 7</span></div>
</section>

<!-- 8 Three cards with photos -->
<section class="slide">
  <div class="h-title">Presentation Title here</div>
  <div class="h-sub">Sub Title Goes Here</div>
  <div class="h-rule"></div>
  <div class="abs" style="left:16px;top:56px;width:305px;display:flex;gap:8px">
    <div class="card-shadow" style="flex:1;height:168px">
      <div class="ph ph-gray" role="img" aria-label="Team group photo" style="position:relative;height:60px"></div>
      <div style="background:var(--navy);color:#fff;font-weight:700;font-size:4.6px;padding:2px 8px">Heading 1</div>
      <ul class="list" style="position:static;padding:5px 8px;font-size:3.8px"><li>Insert Your Heading<br>Text Goes Here</li><li>Lorem ipsum dolor<br>sit amet, consectetur</li><li>Phasellus malesuada<br>vulputate mauris,</li><li>vitae pretium felis<br>vestibulum vel.</li></ul>
    </div>
    <div class="card-shadow" style="flex:1;height:168px">
      <div class="ph ph-warm" role="img" aria-label="Photo of industrial machinery" style="position:relative;height:60px"></div>
      <div style="background:var(--gold);color:#fff;font-weight:700;font-size:4.6px;padding:2px 8px">Heading 2</div>
      <ul class="list" style="position:static;padding:5px 8px;font-size:3.8px"><li>Insert Your Heading<br>Text Goes Here</li><li>Lorem ipsum dolor<br>sit amet, consectetur</li><li>Phasellus malesuada<br>vulputate mauris,</li><li>vitae pretium felis<br>vestibulum vel.</li></ul>
    </div>
    <div class="card-shadow" style="flex:1;height:168px">
      <div class="ph ph-dark" role="img" aria-label="Photo of a team at an event" style="position:relative;height:60px"></div>
      <div style="background:var(--sky);color:#fff;font-weight:700;font-size:4.6px;padding:2px 8px">Heading 3</div>
      <ul class="list" style="position:static;padding:5px 8px;font-size:3.8px"><li>Insert Your Heading<br>Text Goes Here</li><li>Lorem ipsum dolor<br>sit amet, consectetur</li><li>Phasellus malesuada<br>vulputate mauris,</li><li>vitae pretium felis<br>vestibulum vel.</li></ul>
    </div>
  </div>
  <div class="note">Footnote sample: Lorem ipsum dolor sit amet, te ullum corpora delicata duo.</div>
  <div class="foot"><span>WEXFORD LINDQVIST CAPITAL PARTNERS</span><span>CONFIDENTIAL</span><span>wlcpx-example.com &nbsp; 8</span></div>
</section>

<!-- 9 Six point -->
<section class="slide">
  <div class="h-title">6 Poin Content</div>
  <div class="h-sub">Sub Title Goes Here</div>
  <div class="h-rule"></div>
  <div class="abs" style="left:16px;top:70px;width:305px;display:grid;grid-template-columns:repeat(3,1fr);gap:6px 6px">
    <div class="card-shadow" style="height:64px"><div style="background:var(--navy);color:#fff;font-weight:700;font-size:4.6px;padding:5px 8px">Heading Text 1</div><p class="tiny" style="padding:5px 10px">Lorem Ipsum has been the industry's standard dummy text ever since the 1500s, when an unknown printer took a galley of type and scrambled it to make a type specimen book.</p></div>
    <div class="card-shadow" style="height:64px"><div style="background:var(--gold);color:#fff;font-weight:700;font-size:4.6px;padding:5px 8px">Heading Text 2</div><p class="tiny" style="padding:5px 10px">Lorem Ipsum has been the industry's standard dummy text ever since the 1500s, when an unknown printer took a galley of type and scrambled it to make a type specimen book.</p></div>
    <div class="card-shadow" style="height:64px"><div style="background:var(--navy);color:#fff;font-weight:700;font-size:4.6px;padding:5px 8px">Heading Text 3</div><p class="tiny" style="padding:5px 10px">Lorem Ipsum has been the industry's standard dummy text ever since the 1500s, when an unknown printer took a galley of type and scrambled it to make a type specimen book.</p></div>
    <div class="card-shadow" style="height:64px"><div style="background:var(--gold);color:#fff;font-weight:700;font-size:4.6px;padding:5px 8px">Heading Text 4</div><p class="tiny" style="padding:5px 10px">Lorem Ipsum has been the industry's standard dummy text ever since the 1500s, when an unknown printer took a galley of type and scrambled it to make a type specimen book.</p></div>
    <div class="card-shadow" style="height:64px"><div style="background:var(--navy);color:#fff;font-weight:700;font-size:4.6px;padding:5px 8px">Heading Text 5</div><p class="tiny" style="padding:5px 10px">Lorem Ipsum has been the industry's standard dummy text ever since the 1500s, when an unknown printer took a galley of type and scrambled it to make a type specimen book.</p></div>
    <div class="card-shadow" style="height:64px"><div style="background:var(--gold);color:#fff;font-weight:700;font-size:4.6px;padding:5px 8px">Heading Text 6</div><p class="tiny" style="padding:5px 10px">Lorem Ipsum has been the industry's standard dummy text ever since the 1500s, when an unknown printer took a galley of type and scrambled it to make a type specimen book.</p></div>
  </div>
  <div class="note">Footnote sample: Lorem ipsum dolor sit amet, te ullum corpora delicata duo.</div>
  <div class="foot"><span>WEXFORD LINDQVIST CAPITAL PARTNERS</span><span>CONFIDENTIAL</span><span>wlcpx-example.com &nbsp; 9</span></div>
</section>

<!-- 10 Bar chart -->
<section class="slide">
  <div class="h-title">Chart Sample</div>
  <div class="h-sub">Sub Title Goes Here</div>
  <div class="h-rule short"></div>
  <div class="gold-head" style="left:16px;top:56px;color:var(--navy)">Heading Title Here</div>
  <ul class="list" style="left:16px;top:68px;width:160px">
    <li>Lorem ipsum dolor sit amet,<br>te ullum corpora delicata duo.<br>Rebum insolens pri eu.<br>No alia tota modus qui.</li>
    <li class="sub">Sint brute at usu.<br>Duo iisque appareat adversarium at.</li>
    <li>Lorem ipsum dolor sit amet,<br>te ullum corpora delicata duo.<br>Rebum insolens pri eu.<br>No alia tota modus qui.</li>
    <li class="sub">Sint brute at usu.<br>Duo iisque appareat adversarium at.</li>
  </ul>
  <div class="abs" style="left:224px;top:58px;font-size:6px;font-weight:700;color:var(--navy)">Heading Here</div>
  <svg class="abs" style="left:184px;top:66px" width="140" height="160" viewBox="0 0 140 160">
    <g font-size="4.5" fill="#333" font-family="Inter,sans-serif">
      <text x="4" y="8">6</text><text x="4" y="28">5</text><text x="4" y="48">4</text><text x="4" y="68">3</text><text x="4" y="88">2</text><text x="4" y="108">1</text><text x="4" y="128">0</text>
    </g>
    <line x1="14" y1="126" x2="134" y2="126" stroke="#999" stroke-width=".5"/>
    <g>
      <rect x="18" y="40" width="6" height="86" fill="var(--navy)"/><rect x="25" y="78" width="6" height="48" fill="var(--gold)"/><rect x="32" y="86" width="6" height="40" fill="var(--sky)"/>
      <rect x="47" y="76" width="6" height="50" fill="var(--navy)"/><rect x="54" y="38" width="6" height="88" fill="var(--gold)"/><rect x="61" y="86" width="6" height="40" fill="var(--sky)"/>
      <rect x="76" y="56" width="6" height="70" fill="var(--navy)"/><rect x="83" y="90" width="6" height="36" fill="var(--gold)"/><rect x="90" y="66" width="6" height="60" fill="var(--sky)"/>
      <rect x="105" y="36" width="6" height="90" fill="var(--navy)"/><rect x="112" y="70" width="6" height="56" fill="var(--gold)"/><rect x="119" y="26" width="6" height="100" fill="var(--sky)"/>
    </g>
    <g font-size="4.2" fill="#333" font-family="Inter,sans-serif">
      <text x="14" y="135">Category 1</text><text x="44" y="135">Category 2</text><text x="73" y="135">Category 3</text><text x="102" y="135">Category 4</text>
      <rect x="28" y="141" width="3" height="3" fill="var(--navy)"/><text x="33" y="144">Series 1</text>
      <rect x="57" y="141" width="3" height="3" fill="var(--gold)"/><text x="62" y="144">Series 2</text>
      <rect x="86" y="141" width="3" height="3" fill="var(--sky)"/><text x="91" y="144">Series 3</text>
    </g>
  </svg>
  <div class="note">Footnote sample: Lorem ipsum dolor sit amet, te ullum corpora delicata duo.</div>
  <div class="foot"><span>WEXFORD LINDQVIST CAPITAL PARTNERS</span><span>CONFIDENTIAL</span><span>wlcpx-example.com &nbsp; 10</span></div>
</section>

<!-- 11 Pie chart -->
<section class="slide">
  <div class="h-title">Chart Sample</div>
  <div class="h-sub">Sub Title Goes Here</div>
  <div class="h-rule short"></div>
  <div class="gold-head" style="left:16px;top:56px;color:var(--navy)">Heading Title Here</div>
  <ul class="list" style="left:16px;top:68px;width:160px">
    <li>Lorem ipsum dolor sit amet,<br>te ullum corpora delicata duo.<br>Rebum insolens pri eu.<br>No alia tota modus qui.</li>
    <li class="sub">Sint brute at usu.<br>Duo iisque appareat adversarium at.</li>
    <li>Lorem ipsum dolor sit amet,<br>te ullum corpora delicata duo.<br>Rebum insolens pri eu.<br>No alia tota modus qui.</li>
    <li class="sub">Sint brute at usu.<br>Duo iisque appareat adversarium at.</li>
  </ul>
  <div class="abs" style="left:218px;top:56px;font-size:6px;font-weight:700;color:var(--navy)">Heading Here</div>
  <svg class="abs" style="left:190px;top:68px" width="120" height="140" viewBox="0 0 120 140">
    <g stroke="#fff" stroke-width="2">
      <path d="M60 60 L60 22 A38 38 0 0 1 98 60 Z" fill="var(--navy)"/>
      <path d="M60 60 L98 60 A38 38 0 0 1 60 98 Z" fill="var(--gold)"/>
      <path d="M60 60 L60 98 A38 38 0 0 1 22 60 Z" fill="var(--sky)"/>
      <path d="M60 60 L22 60 A38 38 0 0 1 60 22 Z" fill="var(--green)"/>
    </g>
    <g fill="#fff" font-size="7" font-weight="700" font-family="Inter,sans-serif">
      <text x="33" y="46">4.5%</text><text x="70" y="46">4.3%</text><text x="33" y="80">3.5%</text><text x="70" y="80">2.5%</text>
    </g>
    <g fill="#333" font-size="4.2" font-family="Inter,sans-serif">
      <text x="28" y="114">· Category 1</text><text x="66" y="114">· Category 2</text>
      <text x="28" y="122">· Category 3</text><text x="66" y="122">· Category 4</text>
    </g>
  </svg>
  <div class="note">Footnote sample: Lorem ipsum dolor sit amet, te ullum corpora delicata duo.</div>
  <div class="foot"><span>WEXFORD LINDQVIST CAPITAL PARTNERS</span><span>CONFIDENTIAL</span><span>wlcpx-example.com &nbsp; 11</span></div>
</section>

<!-- 12 Donuts -->
<section class="slide">
  <div class="h-title">Chart Sample</div>
  <div class="h-sub">Sub Title Goes Here</div>
  <div class="h-rule short"></div>
  <div class="gold-head" style="left:16px;top:56px;color:var(--navy)">Heading Title Here</div>
  <ul class="list" style="left:16px;top:68px;width:160px">
    <li>Lorem ipsum dolor sit amet,<br>te ullum corpora delicata duo.<br>Rebum insolens pri eu.<br>No alia tota modus qui.</li>
    <li class="sub">Sint brute at usu.<br>Duo iisque appareat adversarium at.</li>
    <li>Lorem ipsum dolor sit amet,<br>te ullum corpora delicata duo.<br>Rebum insolens pri eu.<br>No alia tota modus qui.</li>
    <li class="sub">Sint brute at usu.<br>Duo iisque appareat adversarium at.</li>
  </ul>
  <svg class="abs" style="left:172px;top:88px" width="150" height="90" viewBox="0 0 150 90">
    <circle cx="35" cy="30" r="26" fill="none" stroke="#eee" stroke-width="8"/>
    <circle cx="35" cy="30" r="26" fill="none" stroke="var(--navy)" stroke-width="8" stroke-dasharray="130.7 163.4" transform="rotate(-90 35 30)"/>
    <text x="35" y="33" text-anchor="middle" font-size="9" font-weight="700" fill="var(--navy)" font-family="Inter,sans-serif">80%</text>
    <circle cx="109" cy="30" r="26" fill="none" stroke="#eee" stroke-width="8"/>
    <circle cx="109" cy="30" r="26" fill="none" stroke="var(--gold)" stroke-width="8" stroke-dasharray="98 163.4" transform="rotate(-90 109 30)"/>
    <text x="109" y="33" text-anchor="middle" font-size="9" font-weight="700" fill="var(--gold)" font-family="Inter,sans-serif">60%</text>
    <g font-family="Inter,sans-serif" text-anchor="middle">
      <text x="35" y="69" font-size="5.5" font-weight="700" fill="#222">Data 1</text>
      <text x="35" y="75" font-size="3.8" fill="#555">Lorem ipsum</text><text x="35" y="80" font-size="3.8" fill="#555">dolor sit amet</text>
      <text x="109" y="69" font-size="5.5" font-weight="700" fill="#222">Data 2</text>
      <text x="109" y="75" font-size="3.8" fill="#555">Lorem ipsum</text><text x="109" y="80" font-size="3.8" fill="#555">dolor sit amet</text>
    </g>
  </svg>
  <div class="note">Footnote sample: Lorem ipsum dolor sit amet, te ullum corpora delicata duo.</div>
  <div class="foot"><span>WEXFORD LINDQVIST CAPITAL PARTNERS</span><span>CONFIDENTIAL</span><span>wlcpx-example.com &nbsp; 12</span></div>
</section>

<!-- 13 Photo with content -->
<section class="slide">
  <div class="h-title">Photo With Content</div>
  <div class="h-sub">Sub Title Goes Here</div>
  <div class="h-rule short"></div>
  <div class="gold-head" style="left:16px;top:56px;color:var(--navy)">Heading Title Here</div>
  <ul class="list" style="left:16px;top:68px;width:160px">
    <li>Lorem ipsum dolor sit amet,<br>te ullum corpora delicata duo.<br>Rebum insolens pri eu.<br>No alia tota modus qui.</li>
    <li class="sub">Sint brute at usu.<br>Duo iisque appareat adversarium at.</li>
    <li>Lorem ipsum dolor sit amet,<br>te ullum corpora delicata duo.<br>Rebum insolens pri eu.<br>No alia tota modus qui.</li>
    <li class="sub">Sint brute at usu.<br>Duo iisque appareat adversarium at.</li>
  </ul>
  <div class="ph ph-gray" role="img" aria-label="Photo of two men shaking hands in a warehouse" style="left:181px;top:50px;width:137px;height:162px"></div>
  <div class="note">Footnote sample: Lorem ipsum dolor sit amet, te ullum corpora delicata duo.</div>
  <div class="foot"><span>WEXFORD LINDQVIST CAPITAL PARTNERS</span><span>CONFIDENTIAL</span><span>wlcpx-example.com &nbsp; 13</span></div>
</section>

<!-- 14 Divider green -->
<section class="slide">
  <div class="abs" style="left:14px;top:14px;width:194px;height:222px;background:var(--green)"></div>
  <div class="abs" style="left:14px;top:82px;width:194px;height:60px;background:var(--green-dark)"></div>
  <div class="ph ph-green" role="img" aria-label="Photo of an automated production line with digital overlay" style="left:208px;top:14px;width:115px;height:222px"></div>
  <div class="divider-title" style="left:26px;top:98px">Divider Slide<br>Text Here</div>
  <div class="abs" style="left:26px;top:182px;font-size:5px;color:#fff">Lorem Ipsum is simply dummy text</div>
  <div class="foot"><span>WEXFORD LINDQVIST CAPITAL PARTNERS</span><span>CONFIDENTIAL</span><span>wlcpx-example.com &nbsp; 14</span></div>
</section>

<!-- 15 Process -->
<section class="slide">
  <div class="h-title">Graphic Process Sample</div>
  <div class="h-sub">Sub Title Goes Here</div>
  <div class="h-rule"></div>
  <svg class="abs" style="left:14px;top:72px" width="110" height="110" viewBox="0 0 110 110">
    <circle cx="55" cy="55" r="34" fill="none" stroke="var(--navy)" stroke-width="17" stroke-dasharray="33.6 37.6"/>
    <circle cx="55" cy="55" r="34" fill="none" stroke="var(--gold)" stroke-width="17" stroke-dasharray="33.6 37.6" stroke-dashoffset="-35.6"/>
  </svg>
  <div class="abs" style="left:140px;top:72px;width:180px;display:flex;flex-direction:column;gap:7px">
    <div style="display:flex;gap:7px;align-items:center"><b style="color:var(--navy);font-size:10px;font-family:Archivo,sans-serif">1</b><span class="tiny">Lorem ipsum dolor sit amet, te ullum corpora delicata duo.<br>Rebum insolens pri eu. No alia tota modus qui.</span></div>
    <div style="display:flex;gap:7px;align-items:center"><b style="color:var(--navy);font-size:10px;font-family:Archivo,sans-serif">2</b><span class="tiny">Lorem ipsum dolor sit amet, te ullum corpora delicata duo.<br>Rebum insolens pri eu. No alia tota modus qui.</span></div>
    <div style="display:flex;gap:7px;align-items:center"><b style="color:var(--navy);font-size:10px;font-family:Archivo,sans-serif">3</b><span class="tiny">Lorem ipsum dolor sit amet, te ullum corpora delicata duo.<br>Rebum insolens pri eu. No alia tota modus qui.</span></div>
    <div style="display:flex;gap:7px;align-items:center"><b style="color:var(--navy);font-size:10px;font-family:Archivo,sans-serif">4</b><span class="tiny">Lorem ipsum dolor sit amet, te ullum corpora delicata duo.<br>Rebum insolens pri eu. No alia tota modus qui.</span></div>
    <div style="display:flex;gap:7px;align-items:center"><b style="color:var(--navy);font-size:10px;font-family:Archivo,sans-serif">5</b><span class="tiny">Lorem ipsum dolor sit amet, te ullum corpora delicata duo.<br>Rebum insolens pri eu. No alia tota modus qui.</span></div>
    <div style="display:flex;gap:7px;align-items:center"><b style="color:var(--navy);font-size:10px;font-family:Archivo,sans-serif">6</b><span class="tiny">Lorem ipsum dolor sit amet, te ullum corpora delicata duo.<br>Rebum insolens pri eu. No alia tota modus qui.</span></div>
  </div>
  <div class="note">Footnote sample: Lorem ipsum dolor sit amet, te ullum corpora delicata duo.</div>
  <div class="foot"><span>WEXFORD LINDQVIST CAPITAL PARTNERS</span><span>CONFIDENTIAL</span><span>wlcpx-example.com &nbsp; 15</span></div>
</section>

<!-- 16 Pyramid -->
<section class="slide">
  <div class="h-title" style="left:18px">Presentation Title Here</div>
  <div class="h-sub" style="left:18px">Sub Title Goes Here</div>
  <div class="h-rule"></div>
  <svg class="abs" style="left:36px;top:72px" width="160" height="130" viewBox="0 0 160 130">
    <polygon points="80,0 100,34 60,34" fill="var(--navy)"/>
    <polygon points="56,41 104,41 126,80 34,80" fill="var(--gold)"/>
    <polygon points="30,87 130,87 152,124 8,124" fill="var(--sky)"/>
  </svg>
  <div class="abs" style="left:148px;top:76px"><b style="font-size:7px;color:var(--navy)">High</b><p class="tiny">Lorem ipsum dolor sit amet, te ullum corpora delicata<br>duo. Rebum insolens pri eu. No alia tota modus qui.</p></div>
  <div class="abs" style="left:166px;top:120px"><b style="font-size:7px;color:var(--gold)">Middle</b><p class="tiny">Lorem ipsum dolor sit amet, te ullum corpora delicata<br>duo. Rebum insolens pri eu. No alia tota modus qui.</p></div>
  <div class="abs" style="left:194px;top:168px"><b style="font-size:7px;color:var(--sky)">Low</b><p class="tiny">Lorem ipsum dolor sit amet, te ullum corpora delicata<br>duo. Rebum insolens pri eu. No alia tota modus qui.</p></div>
  <div class="note">Footnote sample: Lorem ipsum dolor sit amet, te ullum corpora delicata duo.</div>
  <div class="foot"><span>WEXFORD LINDQVIST CAPITAL PARTNERS</span><span>CONFIDENTIAL</span><span>wlcpx-example.com &nbsp; 16</span></div>
</section>

<!-- 17 Text with boxes and quote -->
<section class="slide">
  <div class="h-title">Presentation Title Here</div>
  <div class="h-sub">Sub Title Goes Here</div>
  <div class="h-rule"></div>
  <ul class="list" style="left:16px;top:56px;width:112px;font-size:5.2px">
    <li>Lorem ipsum dolor sit amet, consectetur adipiscing elit. Phasellus malesuada vulputate mauris, vitae pretium felis vestibulum vel. Vestibulum non sagittis orci. Fusce finibus elit et felis imperdiet</li>
    <li>Lorem ipsum dolor sit amet, consectetur adipiscing elit. Phasellus malesuada vulputate mauris, vitae pretium felis vestibulum vel. Vestibulum non sagittis orci. Fusce finibus elit et felis imperdiet</li>
  </ul>
  <div class="abs" style="left:136px;top:52px;width:88px;height:92px;background:var(--navy);color:#fff;padding:22px 5px 0;font-size:4.3px;line-height:1.3">Lorem ipsum dolor sit amet, consectetur adipiscing elit. Phasellus malesuada vulputate mauris, vitae pretium felis vestibulum vel. Vestibulum non sagittis orci. Fusce finibus elit et felis imperdiet</div>
  <div class="abs" style="left:230px;top:52px;width:88px;height:92px;background:var(--gold);color:#fff;padding:22px 5px 0;font-size:4.3px;line-height:1.3">Lorem ipsum dolor sit amet, consectetur adipiscing elit. Phasellus malesuada vulputate mauris, vitae pretium felis vestibulum vel. Vestibulum non sagittis orci. Fusce finibus elit et felis imperdiet</div>
  <div class="abs" style="left:136px;top:150px;width:182px;height:44px;background:var(--sky);color:#fff;padding:6px 8px;font-size:4.3px;line-height:1.3"><b style="font-size:8px;font-family:Archivo,sans-serif">“</b> Lorem ipsum dolor sit amet, consectetur adipiscing elit. Phasellus malesuada vulputate mauris, vitae pretium felis vestibulum vel.<div style="text-align:right;margin-top:4px">- Lorem Ipsum</div></div>
  <div class="note">Footnote sample: Lorem ipsum dolor sit amet, te ullum corpora delicata duo.</div>
  <div class="foot"><span>WEXFORD LINDQVIST CAPITAL PARTNERS</span><span>CONFIDENTIAL</span><span>wlcpx-example.com &nbsp; 17</span></div>
</section>

<!-- 18 About us -->
<section class="slide">
  <div class="h-title">About Us</div>
  <div class="h-sub">Sub Title Goes Here</div>
  <div class="h-rule"></div>
  <div class="abs" style="left:16px;top:56px;width:305px;display:flex;gap:6px">
    <div class="card-shadow" style="flex:1;height:132px"><div style="background:var(--navy);color:#fff;font-weight:700;font-size:4.6px;padding:7px 10px 7px 22px;height:32px">Heading<br>Text 1</div><p class="tiny" style="padding:5px">Lorem ipsum dolor sit amet, consectetur adipiscing elit. Phasellus malesuada vulputate mauris, vitae pretium felis vestibulum vel. Vestibulum non sagittis orci. Fusce finibus elit et felis imperdiet</p></div>
    <div class="card-shadow" style="flex:1;height:132px"><div style="background:var(--gold);color:#fff;font-weight:700;font-size:4.6px;padding:7px 10px 7px 22px;height:32px">Heading<br>Text 2</div><p class="tiny" style="padding:5px">Lorem ipsum dolor sit amet, consectetur adipiscing elit. Phasellus malesuada vulputate mauris, vitae pretium felis vestibulum vel. Vestibulum non sagittis orci. Fusce finibus elit et felis imperdiet</p></div>
    <div class="card-shadow" style="flex:1;height:132px"><div style="background:var(--navy);color:#fff;font-weight:700;font-size:4.6px;padding:7px 10px 7px 22px;height:32px">Heading<br>Text 3</div><p class="tiny" style="padding:5px">Lorem ipsum dolor sit amet, consectetur adipiscing elit. Phasellus malesuada vulputate mauris, vitae pretium felis vestibulum vel. Vestibulum non sagittis orci. Fusce finibus elit et felis imperdiet</p></div>
    <div class="card-shadow" style="flex:1;height:132px"><div style="background:var(--gold);color:#fff;font-weight:700;font-size:4.6px;padding:7px 10px 7px 22px;height:32px">Heading<br>Text 4</div><p class="tiny" style="padding:5px">Lorem ipsum dolor sit amet, consectetur adipiscing elit. Phasellus malesuada vulputate mauris, vitae pretium felis vestibulum vel. Vestibulum non sagittis orci. Fusce finibus elit et felis imperdiet</p></div>
  </div>
  <div class="abs" style="left:16px;top:200px;width:305px;height:10px;background:var(--sky);color:#fff;font-size:5.2px;display:flex;align-items:center;justify-content:center">Lorem ipsum dolor sit amet, consectetur adipiscing elit.</div>
  <div class="note">Footnote sample: Lorem ipsum dolor sit amet, te ullum corpora delicata duo.</div>
  <div class="foot"><span>WEXFORD LINDQVIST CAPITAL PARTNERS</span><span>CONFIDENTIAL</span><span>wlcpx-example.com &nbsp; 18</span></div>
</section>

<!-- 19 Team -->
<section class="slide">
  <div class="h-title" style="left:18px">Meet Our Team</div>
  <div class="h-sub" style="left:18px">Sub Title Goes Here</div>
  <div class="h-rule"></div>
  <div class="abs" style="left:18px;top:56px;width:302px;display:flex;gap:6px">
    <div style="flex:1;background:var(--beige);height:152px"><div class="ph ph-gray" role="img" aria-label="Portrait of Warren T. Ashby" style="position:relative;height:104px"></div><div style="padding:6px 6px;font-size:5px;line-height:1.3"><b style="color:var(--gold)">Warren T. Ashby</b><br>Managing Partner</div></div>
    <div style="flex:1;background:var(--beige);height:152px"><div class="ph ph-gray" role="img" aria-label="Portrait of Daniel R. Moreau" style="position:relative;height:104px"></div><div style="padding:6px 6px;font-size:5px;line-height:1.3"><b style="color:var(--gold)">Daniel R. Moreau</b><br>Partner</div></div>
    <div style="flex:1;background:var(--beige);height:152px"><div class="ph ph-gray" role="img" aria-label="Portrait of Colin F. Brightwater" style="position:relative;height:104px"></div><div style="padding:6px 6px;font-size:5px;line-height:1.3"><b style="color:var(--gold)">Colin F.</b><br>Brightwater Partner</div></div>
    <div style="flex:1;background:var(--beige);height:152px"><div class="ph ph-gray" role="img" aria-label="Portrait of Martin J. Kessler" style="position:relative;height:104px"></div><div style="padding:6px 6px;font-size:5px;line-height:1.3"><b style="color:var(--gold)">Martin J. Kessler</b><br>Managing Director</div></div>
  </div>
  <div class="note">Footnote sample: Lorem ipsum dolor sit amet, te ullum corpora delicata duo.</div>
  <div class="foot"><span>WEXFORD LINDQVIST CAPITAL PARTNERS</span><span>CONFIDENTIAL</span><span>wlcpx-example.com &nbsp; 19</span></div>
</section>

<!-- 20 Quote -->
<section class="slide">
  <div class="ph ph-gray" role="img" aria-label="Portrait of Martin J. Kessler" style="left:0;top:0;width:123px;height:243px"></div>
  <div class="abs" style="left:0;top:212px;width:123px;height:31px;background:var(--navy);color:#fff;padding:5px 9px"><div style="font-family:Archivo,sans-serif;font-weight:700;font-size:9px">Martin J. Kessler</div><div style="font-size:5px">Managing Director</div></div>
  <div class="abs" style="left:145px;top:50px;font-family:Archivo,sans-serif;font-weight:900;font-size:28px;color:var(--navy);line-height:1">“</div>
  <div class="abs" style="left:145px;top:74px;width:175px;font-size:5.2px;font-weight:700;line-height:1.3">Lorem Ipsum has been the industry's standard dummy text ever since the 1500s, <span style="color:var(--sky)">when an unknown printer took a galley of type</span> and scrambled it to make a type specimen book.</div>
  <div class="abs" style="left:145px;top:114px;width:175px;font-size:4.4px;line-height:1.3">Lorem Ipsum is simply dummy text of the printing and typesetting industry. Lorem Ipsum has been the industry's standard dummy text ever since the 1500s, when an unknown printer took a galley of type and scrambled it to make a type specimen book. It has survived not only five centuries, but also the leap into electronic typesetting, remaining essentially unchanged. It was popularised in the 1960s with the release of Letraset sheets containing Lorem Ipsum passages, and more recently with desktop publishing software including versions of Lorem Ipsum.</div>
  <div class="abs" style="left:145px;bottom:14px;font-size:3.2px;color:#aaa">Footnote sample: Lorem ipsum dolor sit amet, te ullum corpora delicata duo.</div>
  <div class="foot"><span>WEXFORD LINDQVIST CAPITAL PARTNERS</span><span>CONFIDENTIAL</span><span>wlcpx-example.com &nbsp; 20</span></div>
</section>

<!-- 21 Thank you -->
<section class="slide">
  <div class="abs" style="left:0;top:0;width:168px;height:252px;background:var(--beige)"></div>
  <div class="abs" style="left:0;top:222px;width:168px;height:2px;background:linear-gradient(90deg,var(--green) 0 33%,var(--gold) 33% 66%,var(--sky) 66%)"></div>
  <div class="abs" style="left:275px;top:0;width:62px;height:146px;background:var(--navy)"></div>
  <div class="wordmark" style="left:16px;top:26px"><span class="dot"></span><span>WEXFORD<br>LINDQVIST<br><small style="font-size:4px;color:var(--gold)">CAPITAL PARTNERS</small></span></div>
  <div class="cover-title" style="left:16px;top:88px;font-size:14px">Thank You</div>
  <div class="abs tiny" style="left:16px;top:108px;font-size:4.4px">Lorem ipsum dolor sit amet, corpora delicata<br>duo. Rebum insolens pri eu.<br>No alia tota modus qui.</div>
  <div class="ph ph-gray" role="img" aria-label="Group photo of the firm's team on outdoor steps" style="left:133px;top:68px;width:176px;height:112px"></div>
  <div class="abs" style="left:16px;top:164px;display:flex;flex-direction:column;gap:8px;font-size:5.5px">
    <div style="display:flex;align-items:center;gap:4px"><span style="width:7px;height:7px;border-radius:50%;background:var(--navy)"></span>yourmail@website.com</div>
    <div style="display:flex;align-items:center;gap:4px"><span style="width:7px;height:7px;border-radius:50%;background:var(--gold)"></span>+1234 5678 910</div>
    <div style="display:flex;align-items:center;gap:4px"><span style="width:7px;height:7px;border-radius:50%;background:var(--sky)"></span>www.yourwebsite.com</div>
  </div>
</section>

</main>
</body>
</html>
```